A compelling brochure for a children's charity to encourage donations

We are looking for a 4-page A-4 booklet (1 x A3 page folded in half). the Hour of Kindness Foundation is a non-profit organisation that aims to reduce the incidence and impact of children's critical injury in Australia. The brochure will give people who are new to the charity, an overview of who we are, what we do, why we do it and how they can help. You can reference our website www.hourofkindness-kids.org.au for colours and styles. The final design should encourage people to make a donation by being positive and powerful.
Use the text in the uploaded files.
Non-Profit

```html
<!DOCTYPE html>
<html lang="en">
<head>
<meta charset="utf-8">
<title>Hour of Kindness Foundation – Brochure Page</title>
<link href="https://fonts.googleapis.com/css2?family=Cabin:ital,wght@0,400;0,600;1,400&display=swap" rel="stylesheet">
<style>
  :root {
    --ink: #2b2a28;
    --magenta: #c0197a;
    --orange: #f2a81d;
    --paper: #ffffff;
  }
  * { margin: 0; padding: 0; box-sizing: border-box; }
  html, body { width: 848px; height: 1200px; overflow: hidden; background: var(--paper); }
  .page {
    position: relative; width: 848px; height: 1200px; overflow: hidden;
    font-family: "Cabin", "Trebuchet MS", sans-serif; color: var(--ink);
    hyphens: auto; -webkit-hyphens: auto;
    background:
      radial-gradient(ellipse 170px 260px at 60px 170px, rgba(243,198,230,.75), transparent 70%),
      radial-gradient(ellipse 260px 380px at 130px 560px, rgba(251,216,154,.7), transparent 70%),
      radial-gradient(ellipse 200px 260px at 300px 120px, rgba(251,216,154,.55), transparent 70%),
      radial-gradient(ellipse 150px 220px at 40px 850px, rgba(243,198,230,.55), transparent 70%),
      radial-gradient(ellipse 230px 300px at 60px 1000px, rgba(251,216,154,.55), transparent 70%),
      var(--paper);
  }
  .edge-lines { position: absolute; top: 0; left: 0; }
  .brand {
    position: absolute; left: 490px; top: 58px; width: 280px;
    font-size: 28px; font-weight: 600; line-height: 34px; color: var(--ink);
  }
  .brand-url { position: absolute; left: 490px; top: 152px; font-size: 19px; color: var(--orange); }
  .facts { position: absolute; left: 38px; top: 28px; font-size: 15.6px; line-height: 19.6px; }
  .facts-intro { margin-bottom: 19px; font-size: 15px; }
  .facts ul { list-style: none; }
  .facts li { text-align: justify; }
  .facts li::before { content: "• "; }
  .narrow { width: 434px; }
  .wide { width: 727px; }
  .copy { position: absolute; left: 38px; width: 727px; font-size: 19.6px; line-height: 25.8px; text-align: justify; }
  .copy .gap { margin-top: 25.8px; }
  .call { position: absolute; left: 38px; top: 810px; width: 482px; font-size: 19.2px; font-weight: 600; line-height: 26px; text-align: justify; }
  .note { position: absolute; left: 38px; top: 990px; width: 482px; font-size: 18.6px; font-style: italic; line-height: 25.6px; }
  .hands {
    position: absolute; left: 525px; top: 910px; width: 255px; height: 285px;
    background: radial-gradient(circle at 30% 25%, rgba(160,70,200,.35), transparent 40%),
                radial-gradient(circle at 82% 20%, rgba(230,40,40,.35), transparent 40%),
                radial-gradient(circle at 55% 55%, rgba(60,170,40,.4), transparent 45%),
                radial-gradient(circle at 75% 90%, rgba(30,60,220,.35), transparent 40%),
                radial-gradient(circle at 25% 88%, rgba(240,220,30,.45), transparent 40%);
  }
</style>
</head>
<body>
<div class="page">
  <svg class="edge-lines" width="848" height="1200" aria-hidden="true">
    <path d="M785 30 C783 300 788 600 784 900 C783 1050 786 1150 785 1195" stroke="var(--magenta)" stroke-width="3.5" fill="none"/>
    <path d="M802 0 C800 300 804 700 801 1200" stroke="var(--magenta)" stroke-width="1.5" fill="none" opacity=".7"/>
    <path d="M806 0 C808 250 804 500 807 640" stroke="var(--orange)" stroke-width="2.5" fill="none"/>
    <path d="M805 560 C807 700 803 900 806 1200" stroke="var(--orange)" stroke-width="1.5" fill="none" opacity=".6"/>
    <path d="M30 1112 C200 1109 420 1114 652 1110" stroke="var(--orange)" stroke-width="3" fill="none"/>
  </svg>

  <div class="brand">Hour of Kindness Foundation</div>
  <div class="brand-url">www.hourofkindness-kids.org.au</div>

  <section class="facts">
    <p class="facts-intro">Did you know.....</p>
    <ul>
      <li class="narrow">Injury is the leading cause of death for children aged between 1 and 14 in Australia.</li>
      <li class="narrow">Approximately 1000 children are hospitalised each week; more than twice the number of children hospitalised with cancer, diabetes and asthma combined.</li>
      <li class="narrow">More than 40% of parents of critically injured children suffer depression</li>
      <li class="wide">Severely injured children are three to six times more likely to survive their injuries if they receive definitive care at a paediatric trauma centre.</li>
      <li class="wide">Child injury is of such public health importance that the Australian government recently identified children aged 0-14 as a priority issue, but has not yet implemented any nationally coordinated injury prevention strategies to address it.</li>
    </ul>
  </section>

  <section class="copy" style="top:318px">
    <p>In 2012, a commissioned study by Dr Helen Marsh of the University of the Southern Coast revealed a lack of centralised national data relating to children’s critical injury despite alarming statistics.</p>
    <p class="gap">Dr Marsh’s study discovered that parents of injured children experience myriad emotional, mental and physical stressors which result in anxiety, depression, addictions, job-loss and collapse of the family unit. 60% of these parents are likely to meet the criteria for Acute Stress Disorder and 70% of parents report fatigue 6 months after their child’s discharge.</p>
    <p>A parent’s ability to cope with the stress associated with the injury will affect the quality of life of all members of the family, as parents have total responsibility for practical considerations such as accommodation, jobs, other children, transport, bill payment as well as and holistic implications, however little is known from an Australian perspective with a paucity of evidence-based recommendations or solutions.</p>
    <p class="gap">Over several years, the Foundation delivered specialised medical equipment, technologically innovative machines, therapies and individual services to hospitals and families across the country.</p>
  </section>

  <p class="call">However, to permanently reduce the incidence and impact of children’s critical injuries, we must better understand the breadth and depths of the challenges faced by these children and their families throughout the trauma journey, and assess the health-care system’s efficacy in addressing these challenges.</p>

  <p class="note">Presently in Australia, we do not have adequate knowledge about who is injured, where they come from, what causes the injuries, how the families cope and whether or not families survive intact in the longer term.</p>

  <div class="hands" role="img" aria-label="Colourful children's painted handprints in purple, red, green, yellow and blue"></div>
</div>
</body>
</html>
```